Icons/images for company values

We have five company values, we have a new logo and a new look. I would like drawn images for each value that are in keeping with our look and feel.

Target Market(s)

internal/staff

Industry/Entity Type

media compliance

Requirements
Must have
• colours aligned with logo.

```html
<!DOCTYPE html>
<html lang="en">
<head>
<meta charset="utf-8">
<title>Values 2023</title>
<link rel="stylesheet" href="https://fonts.googleapis.com/css2?family=Poppins:wght@300;500;600;700;800&display=swap">
<style>
  :root {
    --navy: #0b6689;
    --gold: #fcdd48;
    --ink: #0d2a35;
    --icon: #0d5a7a;
    --brand-blue: #1a8fc0;
    --green-top: #6fe3a0;
    --green-bottom: #4cc07f;
    --lime-top: #8fef8a;
    --lime-bottom: #5ad6a0;
    --blue-top: #1593cc;
    --blue-bottom: #0a7ab8;
    --teal-top: #52c8d4;
    --teal-bottom: #2aaab8;
    --yellow-top: #c6e86a;
    --yellow-bottom: #fcdd48;
    --stage: #e6e6e6;
  }
  * { box-sizing: border-box; margin: 0; padding: 0; }
  html, body { width: 1200px; height: 1054px; overflow: hidden; }
  body {
    background: var(--stage);
    font-family: "Poppins", sans-serif;
    color: var(--ink);
  }
  .poster {
    position: absolute;
    left: 0; top: 102px;
    width: 1200px; height: 849px;
    background: radial-gradient(ellipse at 50% 45%, #ffffff 0%, #f2f2f2 45%, #d9d9d9 100%);
    overflow: hidden;
  }
  .map-backdrop {
    position: absolute;
    left: 20px; top: 190px; width: 1180px; height: 600px;
    background: radial-gradient(ellipse at 50% 45%, rgba(150,150,150,0.16) 0%, rgba(150,150,150,0.08) 55%, rgba(150,150,150,0) 75%);
  }
  .title-pill {
    position: absolute;
    left: 238px; top: 61px; width: 714px; height: 116px;
    border-radius: 58px;
    background: var(--navy);
    box-shadow: 0 8px 12px rgba(0,0,0,0.18);
    display: flex; align-items: center; justify-content: center;
    font-weight: 800; font-size: 84px; letter-spacing: 1px;
    color: #ffffff; line-height: 1;
  }
  .title-pill .year { color: var(--gold); margin-left: 20px; }
  .connectors { position: absolute; left: 0; top: 0; }
  .hub { position: absolute; left: 469px; top: 225px; width: 252px; height: 252px; }
  .hub-name {
    position: absolute; left: 469px; top: 225px; width: 252px; height: 252px;
    display: flex; align-items: center; justify-content: center;
    font-weight: 300; font-size: 30px; letter-spacing: 14px;
    color: var(--brand-blue); padding-left: 14px;
  }
  .value-card {
    position: absolute;
    border-radius: 40px;
    box-shadow: 0 6px 10px rgba(0,0,0,0.18);
    padding: 26px 14px 0 91px;
  }
  .value-card h2 {
    font-weight: 700; font-size: 17px; line-height: 21px;
    text-transform: uppercase; letter-spacing: -0.2px;
  }
  .value-card p {
    font-weight: 500; font-size: 11.3px; line-height: 14px;
    margin-top: 14px;
  }
  .value-card.two-line h2 { margin-top: -8px; }
  .value-card.two-line p { margin-top: 11px; }
  .icon-badge {
    position: absolute; left: 9px; top: 50%;
    width: 72px; height: 72px; margin-top: -36px;
    border-radius: 50%; background: #ffffff;
    border: 5px solid rgba(255,255,255,0.55);
    background-clip: padding-box;
    box-shadow: 0 3px 6px rgba(0,0,0,0.25);
    display: flex; align-items: center; justify-content: center;
  }
  .icon-badge svg { width: 40px; height: 40px; }
  .card-open { left: 44px; top: 281px; width: 384px; height: 126px;
    background: linear-gradient(var(--green-top) 50%, var(--green-bottom) 50%); }
  .card-done { left: 755px; top: 279px; width: 399px; height: 128px;
    background: linear-gradient(var(--lime-top) 50%, var(--lime-bottom) 50%); }
  .card-done p { margin-top: 18px; }
  .card-faster { left: 87px; top: 459px; width: 384px; height: 128px;
    background: linear-gradient(var(--blue-top) 50%, var(--blue-bottom) 50%); }
  .card-diverse { left: 709px; top: 457px; width: 400px; height: 129px;
    background: linear-gradient(var(--teal-top) 50%, var(--teal-bottom) 50%); }
  .card-leaders { left: 384px; top: 629px; width: 412px; height: 129px;
    background: linear-gradient(var(--yellow-top) 50%, var(--yellow-bottom) 50%); }
</style>
</head>
<body>
<main class="poster">
  <div class="map-backdrop" role="img" aria-label="Faint grey world map in the background"></div>

  <h1 class="title-pill">VALUES<span class="year">2023</span></h1>

  <svg class="connectors" width="1200" height="849" viewBox="0 0 1200 849" aria-hidden="true">
    <line x1="428" y1="341" x2="475" y2="341" stroke="#7be3a8" stroke-width="6"/>
    <line x1="715" y1="341" x2="760" y2="341" stroke="#8fef8a" stroke-width="6"/>
    <polyline points="576,470 576,520 471,520" fill="none" stroke="#1593cc" stroke-width="6"/>
    <polyline points="615,470 615,520 712,520" fill="none" stroke="#52c8d4" stroke-width="6"/>
    <line x1="595" y1="470" x2="595" y2="632" stroke="#b8e86a" stroke-width="7"/>
  </svg>

  <svg class="hub" viewBox="0 0 252 252" aria-hidden="true">
    <defs>
      <linearGradient id="hubRing" x1="0" y1="0" x2="0" y2="1">
        <stop offset="0" stop-color="#a6f08a"/>
        <stop offset="0.5" stop-color="#6fe0c0"/>
        <stop offset="1" stop-color="#0a7ab8"/>
      </linearGradient>
    </defs>
    <circle cx="126" cy="126" r="123" fill="#ffffff" stroke="#1a8fc0" stroke-width="3"/>
    <circle cx="126" cy="126" r="116" fill="none" stroke="#8fe6a0" stroke-width="4"/>
    <circle cx="126" cy="126" r="104" fill="#ffffff" stroke="url(#hubRing)" stroke-width="18"/>
    <circle cx="126" cy="126" r="95" fill="#ffffff"/>
  </svg>
  <div class="hub-name">KELVA</div>

  <section class="value-card card-open">
    <span class="icon-badge">
      <svg viewBox="0 0 40 40" aria-hidden="true"><path d="M20 34 L6 20 A8 8 0 0 1 20 9 A8 8 0 0 1 34 20 Z" fill="var(--icon)"/><path d="M13 21 l5 5 M17 19 l5 5 M21 17 l5 5" stroke="#fff" stroke-width="2" stroke-linecap="round"/></svg>
    </span>
    <h2>We're open and honest</h2>
    <p>Sharing information helps us achieve the best outcomes for our teams and business. We value open, honest, and clear communication.</p>
  </section>

  <section class="value-card card-done">
    <span class="icon-badge">
      <svg viewBox="0 0 40 40" aria-hidden="true"><circle cx="19" cy="21" r="15" fill="none" stroke="var(--icon)" stroke-width="3.5"/><circle cx="19" cy="21" r="9" fill="none" stroke="var(--icon)" stroke-width="3.5"/><circle cx="19" cy="21" r="3" fill="var(--icon)"/><path d="M19 21 L33 7 M29 5 l5 1 l-1 5" fill="none" stroke="var(--icon)" stroke-width="3" stroke-linecap="round"/></svg>
    </span>
    <h2>We get things done</h2>
    <p>We grow through capability, focus and hard work. We believe small steps compound to big results.</p>
  </section>

  <section class="value-card card-faster two-line">
    <span class="icon-badge">
      <svg viewBox="0 0 40 40" aria-hidden="true"><circle cx="23" cy="22" r="12" fill="none" stroke="var(--icon)" stroke-width="3"/><path d="M23 22 V13 A9 9 0 1 1 14 22 Z" fill="var(--icon)"/><rect x="20" y="4" width="6" height="4" fill="var(--icon)"/><path d="M3 18 h7 M1 23 h8 M4 28 h6" stroke="var(--icon)" stroke-width="2.5" stroke-linecap="round"/></svg>
    </span>
    <h2>We get there faster, together</h2>
    <p>Collaboration is at the heart of what we do, no matter our team.</p>
  </section>

  <section class="value-card card-diverse two-line">
    <span class="icon-badge">
      <svg viewBox="0 0 40 40" aria-hidden="true"><path d="M2 20 Q20 4 38 20 Q20 36 2 20 Z" fill="var(--icon)"/><circle cx="20" cy="20" r="6" fill="#fff"/><circle cx="20" cy="20" r="3" fill="var(--icon)"/><path d="M16 4 l4 -3 l4 3 M16 36 l4 3 l4 -3" fill="none" stroke="var(--icon)" stroke-width="2.5"/></svg>
    </span>
    <h2>Diverse perspectives build better outcomes</h2>
    <p>We value diversity, inclusion, respect and trust within our teams. We are building a truly global organisation.</p>
  </section>

  <section class="value-card card-leaders two-line">
    <span class="icon-badge">
      <svg viewBox="0 0 40 40" aria-hidden="true"><circle cx="13" cy="9" r="4" fill="var(--icon)"/><path d="M8 15 h10 v10 h-2 v12 h-3 v-9 h-1 v9 h-3 v-12 h-1 Z" fill="var(--icon)"/><path d="M24 37 V5" stroke="var(--icon)" stroke-width="2.5"/><path d="M24 5 h12 l-3 4 l3 4 h-12 Z" fill="var(--icon)"/></svg>
    </span>
    <h2>We are leaders in copyright and intellectual property</h2>
    <p>Leading the conversation in audio-visual copyright compliance and advocating for the protection of intellectual property globally.</p>
  </section>
</main>
</body>
</html>
```